Modern Label for Loose Tea pouches on 4.5x6 Label

We need a new label for our teas that is very simple in design, but stylish and modern. This will be used to print labels for our loose tea pouches. The label will be at max 4.5x6 inches in size. There should be a place for the tea name, description, ingredients, and size that is changeable.
Preferably an AI file that allows me to setup variables to change the above items. There will also need to be our logo which is supplied, and our address on the label.
Address:
Quillmere Teas
846 Lower Maple Lane
Fernwick, VT 05612
Target Market(s)
Tea Lovers
Requirements
Must have
- Adobe Illustrator file with variables setup for replacement of tea name, description, ingredients, and size (weights 2oz, 4oz, 8oz, 1lb)

```html
<!DOCTYPE html>
<html lang="en">
<head>
<meta charset="utf-8">
<title>Quillmere Teas – Tea Pouch Label</title>
<link href="https://fonts.googleapis.com/css2?family=Tinos:wght@400;700&family=Arimo:wght@400;700&display=swap" rel="stylesheet">
<style>
  :root {
    --backdrop: #505050;
    --paper: #f1f1f1;
    --paper-shade: #e2e2e2;
    --leaf-light: #b9dc5a;
    --leaf: #8cc63f;
    --leaf-deep: #6fb52c;
    --accent-pink: #d94fa0;
    --title-green: #0a8f44;
    --rule-brown: #8a5a3a;
    --bark: #5b3a22;
    --rust: #a0391f;
    --cocoa: #5a2e0c;
    --illus-tone: #c9d8b8;
  }
  * { box-sizing: border-box; margin: 0; padding: 0; }
  html, body { width: 1200px; height: 1200px; overflow: hidden; }
  body { background: var(--backdrop); position: relative; font-family: "Arimo", Arial, sans-serif; }

  .label {
    position: absolute; left: 222px; top: 96px; width: 758px; height: 1012px;
    background: radial-gradient(ellipse at 50% 45%, var(--paper) 0%, var(--paper) 55%, var(--paper-shade) 100%);
    overflow: hidden;
  }
  .top-band {
    position: absolute; left: 0; top: 0; width: 100%; height: 214px;
    background: radial-gradient(ellipse at 50% 0%, #e4f2a6 0%, var(--leaf-light) 35%, var(--leaf) 100%);
  }
  .top-band-edge { position: absolute; left: 0; top: 214px; width: 100%; height: 4px; background: var(--accent-pink); }
  .bottom-band {
    position: absolute; left: 0; bottom: 0; width: 100%; height: 14px;
    background: linear-gradient(90deg, var(--leaf-deep), #e4f2a6 50%, var(--leaf-deep));
  }

  .brand-seal {
    position: absolute; left: 242px; top: 54px; width: 280px; height: 280px;
    border-radius: 50%; background: #fff; border: 3px solid var(--bark);
    box-shadow: 0 12px 0 rgba(0,0,0,0.28);
    display: flex; align-items: center; justify-content: center;
  }
  .brand-name {
    font-family: "Arimo", Arial, sans-serif; font-weight: 700;
    font-size: 30px; color: var(--rust);
  }

  .tea-name {
    position: absolute; left: 0; top: 343px; width: 100%; text-align: center;
    font-family: "Tinos", "Times New Roman", serif; font-weight: 400; font-size: 98px; line-height: 1;
    color: var(--title-green);
  }
  .tagline {
    position: absolute; left: 208px; top: 444px; width: 348px; height: 34px;
    border-top: 1.5px solid var(--rule-brown); border-bottom: 1.5px solid var(--rule-brown);
    text-align: center; font-family: "Tinos", "Times New Roman", serif;
    font-size: 27px; line-height: 31px; letter-spacing: 1.5px; color: var(--bark);
  }

  .hero-illustration {
    position: absolute; left: 38px; top: 488px; width: 665px; height: 356px;
    background: radial-gradient(ellipse at 50% 50%, #ffffff 0%, #e3e6e3 45%, var(--illus-tone) 75%, rgba(201,216,184,0) 100%);
    border-radius: 50%;
  }

  .claim-seal {
    position: absolute; left: 549px; top: 523px; width: 118px; height: 118px;
    border-radius: 50%; border: 2px solid var(--bark);
  }

  .ingredients { position: absolute; left: 0; top: 852px; width: 100%; text-align: center; }
  .ingredients-title {
    font-family: "Tinos", "Times New Roman", serif; font-weight: 700;
    font-size: 14px; letter-spacing: 0.5px; color: var(--rust);
  }
  .ingredients-text { font-size: 16px; line-height: 20px; color: var(--bark); margin-top: 2px; }

  .weight { position: absolute; left: 44px; top: 929px; }
  .weight-label { font-size: 22px; color: var(--rust); line-height: 1; letter-spacing: -0.3px; }
  .weight-value { font-size: 28px; font-weight: 700; color: var(--cocoa); line-height: 1; margin: 4px 0 0 25px; }

  .address { position: absolute; left: 550px; top: 914px; font-size: 17.5px; line-height: 22px; color: var(--bark); font-style: normal; }
  .address-name { font-weight: 700; color: var(--rust); }
</style>
</head>
<body>
  <main class="label">
    <div class="top-band" role="img" aria-label="Light green band with a soft pattern of tea leaves"></div>
    <div class="top-band-edge"></div>

    <div class="brand-seal"><span class="brand-name">Quillmere Teas</span></div>

    <h1 class="tea-name">Tea Name</h1>
    <p class="tagline">Sip. Pauser. Repart</p>

    <div class="hero-illustration" role="img" aria-label="Illustration of a white cup of tea on a saucer surrounded by fresh green tea leaves"></div>

    <div class="claim-seal" role="img" aria-label="Round product claim seal"></div>

    <section class="ingredients">
      <h2 class="ingredients-title">Ingredients:</h2>
      <p class="ingredients-text">Lorem Ipsum is simply dummy text of the<br>printing and typesetting industry.</p>
    </section>

    <div class="weight">
      <div class="weight-label">WEIGHTS</div>
      <div class="weight-value">2oz</div>
    </div>

    <address class="address">
      <span class="address-name">Quillmere Teas</span><br>
      846 Lower Maple Lane<br>
      Fernwick, VT 05612
    </address>

    <div class="bottom-band"></div>
  </main>
</body>
</html>
```